Medical Clinic Website - New Private Clinic

We have a basic design for a website. Would like it developed in WORDPRESS. the attached JPG shows the page basic design.

Colours and overall design to be similar

MUST BE WORD PRESS and must allow our company to edit at later date. Images must be licenced for use.

The text to be included is:

Target Market(s)

Medical or GP clinic patients

Industry/Entity Type

Medical

Coding

Coded - Design and coding required

Number of Pages Required

1 page

Colors

Designer to choose colors to be used in the design.

Requirements
Must have
• WORDPRESS and use the attached jpg as a design guide.
• Must be able to allow me to insert link to "ember quill" in the top LEFT CORNER. a button or similar. The ember quill designers will help us with this, but it must have the space

```html
<!DOCTYPE html>
<html lang="en">
<head>
<meta charset="utf-8">
<title>Harbourline GP</title>
<link href="https://fonts.googleapis.com/css2?family=Maven+Pro:wght@400;500;600;700&display=swap" rel="stylesheet">
<style>
:root{
  --blue:#1ba6e6;
  --green:#8dbf24;
  --ink:#2b2b2b;
  --muted:#6a6a6a;
  --grey-band:#ececec;
  --footer:#231f20;
  --white:#ffffff;
}
*{margin:0;padding:0;box-sizing:border-box}
html,body{width:669px;height:1200px;overflow:hidden;background:var(--white)}
body{font-family:"Maven Pro",sans-serif;color:var(--ink);position:relative}
.abs{position:absolute}
.btn{position:absolute;display:flex;align-items:center;justify-content:center;font-size:5.6px;font-weight:700;letter-spacing:.3px;color:var(--white);text-transform:uppercase}
.btn--blue{background:var(--blue)}
.btn--green{background:var(--green)}
.btn--white{background:var(--white);color:var(--blue)}

/* header */
.site-header{top:0;left:0;width:669px;height:64px}
.partner-link{left:116px;top:28px;width:69px;height:17px}
.brand{left:0;width:669px;top:24px;display:flex;justify-content:center;align-items:center;gap:5px}
.brand__mark{width:9px;height:9px;background:var(--blue)}
.brand__name{font-size:12px;font-weight:600;color:var(--blue)}
.contact-line{right:117px;display:flex;align-items:center;gap:4px;color:var(--ink)}
.contact-line--phone{top:17px;font-size:10px}
.contact-line--mail{top:35px;font-size:6px}
.contact-line svg{width:12px;height:12px}

/* hero */
.hero{top:64px;left:0;width:669px;height:215px;background:linear-gradient(100deg,#e6eef4 0%,#f3f6f9 40%,#e8eef3 65%,#d4dde5 100%)}
.hero__copy{top:66px;left:0;width:669px;text-align:center;font-size:13.4px;line-height:18px;color:#3a3a3a}
.hero__btn{left:300px;top:131px;width:69px;height:17px}
.hero__arrow{top:101px;width:20px;height:14px}

/* welcome */
.welcome__title{top:305px;width:669px;text-align:center;font-size:14px;font-weight:500}
.rule{position:absolute;width:18px;height:2px;background:var(--blue)}
.welcome__text{top:342px;left:159px;width:351px;text-align:center;font-size:6.3px;line-height:9.7px;color:var(--muted)}
.welcome__btn{left:300px;top:394px;width:69px;height:17px}

/* services */
.services{top:442px;left:0;width:669px;height:270px;background:var(--grey-band)}
.services__title{top:30px;width:669px;text-align:center;font-size:14px;font-weight:500}
.card{top:64px;width:138px;height:163px;background:var(--white)}
.card--raised{box-shadow:0 2px 6px rgba(0,0,0,.15)}
.card__photo{width:138px;height:78px}
.card__title{top:87px;width:100%;text-align:center;font-size:8.4px;font-weight:500;color:#111}
.card__text{top:101px;left:12px;width:114px;text-align:center;font-size:5.9px;line-height:9.4px;color:var(--muted)}
.card__btn{left:38px;top:153px;width:61px;height:16px}

/* appointment */
.appointment{top:743px;left:116px;width:436px;height:189px}
.appointment__panel{left:0;top:0;width:217px;height:189px;background:var(--blue);color:var(--white);text-align:center}
.appointment__icon{left:99px;top:31px;width:19px;height:19px}
.appointment__heading{top:65px;width:100%;font-size:12.6px;font-weight:600;line-height:17.6px}
.appointment__heading .dark{color:#14375a}
.appointment__sub{top:104px;width:100%;font-size:12.8px}
.appointment__btn{left:58px;top:139px;width:101px;height:20px}
.appointment__photo{left:218px;top:0;width:218px;height:189px;background:linear-gradient(110deg,#cfe4f1 0%,#eef3f6 45%,#f4e4e2 100%)}

/* footer */
.site-footer{top:964px;left:0;width:669px;height:236px;background:var(--footer);color:var(--white)}
.footer__title{top:29px;width:669px;text-align:center;font-size:12.8px;font-weight:500}
.footer__col{top:74px;width:150px;text-align:center}
.footer__col svg{display:block;margin:0 auto 7px;width:26px;height:24px}
.footer__label{font-size:7.6px;font-weight:600}
.footer__value{font-size:7px;color:#cfcfcf;line-height:8.6px}
.footer__value--big{font-size:10.6px;letter-spacing:.4px}
.footer__divider{top:73px;height:67px;border-left:1px dotted #555}
.social{top:160px;width:18px;height:18px;border-radius:50%;background:#6d6d6d}
.social--active{background:var(--blue)}
.copyright{top:199px;width:669px;text-align:center;font-size:5.8px;color:#bbbbbb}
.to-top{left:538px;top:184px;width:14px;height:20px}
</style>
</head>
<body>

<header class="site-header abs">
  <a class="btn btn--blue partner-link">Ember Quill</a>
  <div class="brand abs"><span class="brand__mark"></span><span class="brand__name">Harbourline GP</span></div>
  <div class="contact-line contact-line--phone abs">6120 4375
    <svg viewBox="0 0 12 12"><circle cx="6" cy="6" r="6" fill="#1ba6e6"/><path d="M4 3.2l1 1.5-.6.7c.4.8 1 1.4 1.8 1.8l.7-.6 1.5 1-.5 1.1C5.6 8.5 3.5 6.4 3 4z" fill="#fff"/></svg>
  </div>
  <div class="contact-line contact-line--mail abs">reception@harbourlinegp.com.au
    <svg viewBox="0 0 12 12"><circle cx="6" cy="6" r="6" fill="#1ba6e6"/><rect x="3.3" y="4" width="5.4" height="4" fill="#fff"/><path d="M3.3 4l2.7 2 2.7-2" stroke="#1ba6e6" stroke-width=".6" fill="none"/></svg>
  </div>
</header>

<section class="hero abs" role="img" aria-label="Doctor in a white coat with stethoscope writing notes at a desk with a patient">
  <p class="hero__copy abs">Located in north quay, we take appointments and<br>walk in patients, new patientswelcome.<br>All basic and urgent medical</p>
  <a class="btn btn--blue hero__btn">Explore More</a>
  <svg class="hero__arrow abs" style="left:64px" viewBox="0 0 20 14"><path d="M19 7H2M7 2L2 7l5 5" stroke="#222" stroke-width="1.3" fill="none"/></svg>
  <svg class="hero__arrow abs" style="left:583px" viewBox="0 0 20 14"><path d="M1 7h17M13 2l5 5-5 5" stroke="#222" stroke-width="1.3" fill="none"/></svg>
</section>

<section class="welcome">
  <h1 class="welcome__title abs">Welcome to Harbourline GP</h1>
  <span class="rule" style="left:325px;top:327px"></span>
  <p class="welcome__text abs">Lorem ipsum dolor sit amet, consectetur adipiscing elit. Vestibulum ac quam gravida, elementum diam eu, vulputate nulla. Morbi at posuere purus. Praesent condimentum vitae nulla sed luctus. Morbi luctus mattis tortor, vel facilisis lacus tincidunt non. Etiam luctus vestibulum enim sit amet molestie. Donec imperdiet tempus risus sit amet rutrum. Nunc maximus tortor quis blandit ullamcorper.</p>
  <a class="btn btn--green welcome__btn">Explore More</a>
</section>

<section class="services abs">
  <h2 class="services__title abs">Our Services</h2>
  <span class="rule" style="left:325px;top:50px"></span>

  <article class="card abs" style="left:116px">
    <div class="card__photo" role="img" aria-label="Examination room wall with diagnostic instruments" style="background:linear-gradient(160deg,#f2f2f2,#d9dcdf)"></div>
    <h3 class="card__title abs">General Medical Conditions</h3>
    <p class="card__text abs">Lorem ipsum dolor sit amet, consectetur adipiscing elit. Donec tincidunt nisi nec mauris consectetur consectetur.</p>
    <a class="btn btn--blue card__btn">Read More</a>
  </article>

  <article class="card card--raised abs" style="left:265px">
    <div class="card__photo" role="img" aria-label="Gloved hand holding blood sample tubes in a rack" style="background:linear-gradient(160deg,#9fc3d8,#4f6f9a 60%,#b3c9d6)"></div>
    <h3 class="card__title abs">Diagnostic Services</h3>
    <p class="card__text abs">Lorem ipsum dolor sit amet, consectetur adipiscing elit. Donec tincidunt nisi nec mauris consectetur consectetur.</p>
    <a class="btn btn--green card__btn">Read More</a>
  </article>

  <article class="card abs" style="left:415px">
    <div class="card__photo" role="img" aria-label="Physiotherapist treating a patient on a treatment bed" style="background:linear-gradient(160deg,#efe9e4,#c9c3bd)"></div>
    <h3 class="card__title abs">Physiotherapy</h3>
    <p class="card__text abs">Lorem ipsum dolor sit amet, consectetur adipiscing elit. Donec tincidunt nisi nec mauris consectetur consectetur.</p>
    <a class="btn btn--blue card__btn">Read More</a>
  </article>
</section>

<section class="appointment abs">
  <div class="appointment__panel abs">
    <svg class="appointment__icon abs" viewBox="0 0 19 19"><rect x="1.5" y="3" width="16" height="14.5" fill="none" stroke="#fff" stroke-width="1.3"/><path d="M1.5 7h16M5.5 1v4M13.5 1v4" stroke="#fff" stroke-width="1.3"/><path d="M4 9.5h2v2H4zm4.5 0h2v2h-2zm4.5 0h2v2h-2zM4 13h2v2H4zm4.5 0h2v2h-2zm4.5 0h2v2h-2z" fill="#fff"/></svg>
    <h2 class="appointment__heading abs">UNABLE TO GET A<br>DOCTOR'S <span class="dark">APPOINTMENT?</span></h2>
    <p class="appointment__sub abs">We are happy to help</p>
    <a class="btn btn--white appointment__btn">Make an Appointment</a>
  </div>
  <div class="appointment__photo abs" role="img" aria-label="Smiling doctor holding the hands of an elderly patient"></div>
</section>

<footer class="site-footer abs">
  <h2 class="footer__title abs">Contact Us</h2>
  <span class="rule" style="left:325px;top:49px"></span>

  <div class="footer__col abs" style="left:108px">
    <svg viewBox="0 0 26 24"><path d="M8 3l3 4.5-2 2.2c1.2 2.6 3 4.5 5.6 5.8l2.2-2 4.5 3-1.6 3.3C12 19.6 5.4 13 5 5z" fill="none" stroke="#bbb" stroke-width="1"/></svg>
    <div class="footer__label">Call</div>
    <div class="footer__value footer__value--big">6120 4375</div>
  </div>
  <span class="footer__divider abs" style="left:259px"></span>
  <div class="footer__col abs" style="left:259px;top:68px">
    <svg viewBox="0 0 26 24"><path d="M13 23s-7-8-7-13a7 7 0 0114 0c0 5-7 13-7 13z" fill="none" stroke="#bbb" stroke-width="1"/><circle cx="13" cy="10" r="2.6" fill="none" stroke="#bbb" stroke-width="1"/></svg>
    <div class="footer__label">Harbourline GP</div>
    <div class="footer__value">2475 Lorem ipsume, Unit E02,<br>Lorem, ON L7L 0B6</div>
  </div>
  <span class="footer__divider abs" style="left:409px"></span>
  <div class="footer__col abs" style="left:409px">
    <svg viewBox="0 0 26 24"><rect x="1" y="4" width="24" height="16" fill="none" stroke="#bbb" stroke-width="1"/><path d="M1 4l12 9 12-9M1 20l9-8M25 20l-9-8" fill="none" stroke="#bbb" stroke-width="1"/></svg>
    <div class="footer__label">E-mail Us</div>
    <div class="footer__value">reception@harbourlinegp.com.au</div>
  </div>

  <span class="social social--active abs" style="left:297px"></span>
  <span class="social abs" style="left:326px"></span>
  <span class="social abs" style="left:353px"></span>

  <p class="copyright abs">© Copyright 2017 Harbourline GP.. Al Rights Reserved</p>
  <svg class="to-top abs" viewBox="0 0 14 20"><path d="M7 19V2M2 7l5-5 5 5" stroke="#1ba6e6" stroke-width="1.3" fill="none"/></svg>
</footer>

</body>
</html>
```